IT Company based on Biology Business Needs a Business Card Design

We need a business card design for a new company called 'Lumen CELL'. We develop the machine learning solutions especially focused on deep learning algorithms for biology industry. Our initial product is a vision detection on biological images to help doctors diagnose the symptoms. We would like to see designs that use the color green.

Industry/Entity Type

Business

```html
<!DOCTYPE html>
<html lang="en">
<head>
<meta charset="utf-8">
<title>Lumen CELL — Business Card</title>
<link rel="stylesheet" href="https://fonts.googleapis.com/css2?family=Montserrat:wght@400;600;700&family=Open+Sans:wght@400;600&display=swap">
<style>
  :root {
    --page-bg: #eceee9;
    --green-light: #8fd472;
    --green-mid: #35a13c;
    --green-deep: #0b6b2c;
    --green-accent: #5cbf3f;
    --text-green: #2f8f45;
    --title-green: #8cc96b;
    --card-white: #ffffff;
    --shadow: rgba(20, 60, 20, 0.18);
  }
  * { box-sizing: border-box; margin: 0; padding: 0; }
  html, body {
    width: 1200px; height: 913px; overflow: hidden;
    background: var(--page-bg);
  }
  .canvas {
    position: relative; width: 1200px; height: 913px;
    display: flex; align-items: center; justify-content: center; gap: 60px;
  }
  .card {
    position: relative; width: 525px; height: 300px;
    border-radius: 4px; overflow: hidden;
    box-shadow: 0 10px 28px var(--shadow);
  }
  /* Front */
  .card-front {
    background: linear-gradient(150deg, var(--green-light) 0%, var(--green-mid) 38%, var(--green-deep) 100%);
    display: flex; align-items: center; justify-content: center;
  }
  .brand {
    display: flex; align-items: center; gap: 16px;
    color: var(--card-white);
    font-family: "Montserrat", sans-serif; font-weight: 400;
    font-size: 40px; letter-spacing: 1px;
  }
  .brand-dot {
    width: 22px; height: 22px; border-radius: 50%;
    background: var(--card-white);
  }
  /* Back */
  .card-back { background: var(--card-white); }
  .card-back .wave { position: absolute; inset: 0; }
  .back-brand {
    position: absolute; left: 40px; top: 196px;
    color: var(--card-white);
    font-family: "Montserrat", sans-serif; font-weight: 400;
    font-size: 26px; letter-spacing: 1px;
  }
  .contact {
    position: absolute; left: 282px; top: 40px; width: 230px;
    font-family: "Open Sans", sans-serif; color: var(--text-green);
  }
  .person-name {
    font-family: "Montserrat", sans-serif; font-weight: 700;
    font-size: 21px; color: var(--text-green);
  }
  .person-title {
    font-size: 11px; color: var(--title-green); margin-top: 2px;
  }
  .details { list-style: none; margin-top: 34px; font-size: 11.5px; line-height: 1.55; }
  .details li { display: flex; align-items: flex-start; gap: 8px; }
  .details svg { flex: 0 0 11px; width: 11px; height: 11px; margin-top: 3px; fill: var(--text-green); }
  .details .address { margin-top: 6px; padding-left: 19px; display: block; }
</style>
</head>
<body>
<main class="canvas">
  <section class="card card-front" aria-label="Card front">
    <div class="brand"><span class="brand-dot"></span><span>Lumen CELL</span></div>
  </section>

  <section class="card card-back" aria-label="Card back">
    <svg class="wave" viewBox="0 0 525 300" preserveAspectRatio="none" aria-hidden="true">
      <defs>
        <linearGradient id="backGreen" x1="0" y1="0" x2="1" y2="1">
          <stop offset="0" stop-color="#6cc94a"/>
          <stop offset="0.5" stop-color="#1d8a3a"/>
          <stop offset="1" stop-color="#0b6b2c"/>
        </linearGradient>
      </defs>
      <path d="M0 40 C120 30 190 70 230 140 C255 190 262 250 280 300 L0 300 Z" fill="#5cbf3f"/>
      <path d="M0 46 C110 38 175 78 214 145 C238 192 246 250 262 300 L0 300 Z" fill="url(#backGreen)"/>
    </svg>
    <div class="back-brand">Lumen CELL</div>
    <div class="contact">
      <h1 class="person-name">Your name</h1>
      <p class="person-title">Your Title</p>
      <ul class="details">
        <li><svg viewBox="0 0 12 12"><path d="M2.5 1h2l1 2.5-1.3 1a6 6 0 0 0 3.3 3.3l1-1.3L11 7.5v2A1.5 1.5 0 0 1 9.5 11 8.5 8.5 0 0 1 1 2.5 1.5 1.5 0 0 1 2.5 1z"/></svg><span>+00 111 222 3333</span></li>
        <li><svg viewBox="0 0 12 12"><path d="M1 2.5h10v7H1z M1.5 3l4.5 3.5L10.5 3" fill="none" stroke="#2f8f45" stroke-width="1.2"/></svg><span>yourname@yourwebsite.com</span></li>
        <li><svg viewBox="0 0 12 12"><circle cx="6" cy="6" r="4.8" fill="none" stroke="#2f8f45" stroke-width="1.1"/><path d="M1.2 6h9.6M6 1.2c-2.5 2.8-2.5 6.8 0 9.6M6 1.2c2.5 2.8 2.5 6.8 0 9.6" fill="none" stroke="#2f8f45" stroke-width="0.9"/></svg><span>www.yourwebsite.com</span></li>
        <li class="address">Your Long Commercial or<br>business address in 2 line</li>
      </ul>
    </div>
  </section>
</main>
</body>
</html>
```